Want to incorporate elements of all these items to make an amazing sign to welcome people to the community. The sign is 6x4 and needs to incorporate the following items:

Welcome to Thistle Grove

Come visit the DWR sales center at 548 marlow road
High Speed Fiber Internet
Land financing starting at $299 (No credit checks)
Let us build your dream home!
517-384-2296
We like the gold and black design no teal or blue that was another agents design. Some combination of the current sign all the stuff listed above and then design elements that tie into the truck wrap.

Target Market(s)

People visiting the neighborhood

Industry/Entity Type

real estate and construction

Font styles to use
Serif

Colors

Designer to choose colors to be used in the design.

Requirements
Must have
• DWR Home Builders Welcomes you to Thistle Grove, Let us build your dream home, Phone number, Land financing starting at $299 NO credit checks

```html
<!DOCTYPE html>
<html lang="en">
<head>
<meta charset="utf-8">
<title>Thistle Grove Welcome Sign</title>
<link rel="stylesheet" href="https://fonts.googleapis.com/css2?family=Lato:ital,wght@0,400;0,700;0,900;1,400&family=Oswald:wght@400;500&display=swap">
<style>
  :root {
    --backdrop: #e4e3e7;
    --black-top: #3a3a3a;
    --black-bottom: #0b0b0b;
    --band-dark: #231f20;
    --gold: #a9894a;
    --white: #ffffff;
    --ink: #1a1a1a;
  }
  * { margin: 0; padding: 0; box-sizing: border-box; }
  html, body { width: 1023px; height: 1200px; overflow: hidden; background: var(--backdrop); }
  .welcome-sign {
    position: absolute; left: 32px; top: 280px; width: 960px; height: 640px;
    font-family: "Lato", Arial, sans-serif; box-shadow: 0 6px 18px rgba(0,0,0,.18);
    overflow: hidden;
  }
  .sign-shapes { position: absolute; inset: 0; width: 100%; height: 100%; }
  .sign-text { position: absolute; line-height: 1; white-space: nowrap; }
  .greeting { left: 47px; top: 46px; font-size: 40px; color: var(--white); }
  .community-name { left: 40px; top: 108px; font-size: 116px; font-weight: 900; line-height: .96; color: var(--white); letter-spacing: -1px; }
  .visit-lead { left: 47px; top: 378px; font-size: 34px; color: var(--gold); }
  .sales-center { left: 47px; top: 420px; display: flex; align-items: center; gap: 12px; color: var(--white); }
  .sales-center .brand { font-family: "Oswald", Arial, sans-serif; font-size: 96px; font-weight: 500; line-height: 1; }
  .sales-center .label { font-size: 42px; line-height: 1; }
  .address { left: 50px; top: 526px; font-size: 31px; color: var(--gold); }
  .right { right: 44px; text-align: right; }
  .offer-head { top: 25px; font-size: 34px; font-weight: 700; color: var(--gold); }
  .offer-item { top: 82px; font-size: 37px; font-weight: 700; line-height: 42px; color: var(--ink); }
  .financing { top: 197px; font-size: 36px; line-height: 37px; color: var(--white); }
  .price { top: 262px; font-family: "Oswald", Arial, sans-serif; font-size: 118px; font-weight: 500; color: var(--gold); }
  .fine-print { top: 380px; font-size: 26px; font-style: italic; color: var(--white); }
  .tagline { right: 190px; top: 461px; text-align: right; font-size: 34px; line-height: 36px; color: var(--ink); }
  .call { top: 455px; font-size: 74px; font-weight: 700; color: var(--gold); }
  .phone { top: 532px; font-size: 72px; font-weight: 900; color: var(--ink); }
</style>
</head>
<body>
  <section class="welcome-sign">
    <svg class="sign-shapes" viewBox="0 0 618 412" preserveAspectRatio="none" aria-hidden="true">
      <defs>
        <linearGradient id="panelBlack" x1="0" y1="0" x2="0" y2="1">
          <stop offset="0" stop-color="var(--black-top)"/>
          <stop offset="1" stop-color="var(--black-bottom)"/>
        </linearGradient>
        <clipPath id="rightColumn">
          <path d="M450,0 L618,0 L618,412 L170,412 C340,330 420,180 450,0 Z"/>
        </clipPath>
      </defs>
      <rect width="618" height="412" fill="url(#panelBlack)"/>
      <path d="M450,0 L618,0 L618,412 L170,412 C340,330 420,180 450,0 Z" fill="var(--white)"/>
      <rect x="0" y="118" width="618" height="159" fill="var(--band-dark)" clip-path="url(#rightColumn)"/>
      <path d="M400,0 L450,0 C420,180 340,330 170,412 C290,330 385,180 400,0 Z" fill="var(--gold)"/>
    </svg>

    <p class="sign-text greeting">Welcome to</p>
    <h1 class="sign-text community-name">THISTLE<br>GROVE</h1>
    <p class="sign-text visit-lead">Come visit the</p>
    <p class="sign-text sales-center"><span class="brand">DWR</span><span class="label">sales<br>center</span></p>
    <p class="sign-text address">at 548 marlow road</p>

    <p class="sign-text right offer-head">WE OFFER</p>
    <p class="sign-text right offer-item">High Speed<br>Fiber Internet</p>
    <p class="sign-text right financing">Land financing<br>starting at</p>
    <p class="sign-text right price">$299</p>
    <p class="sign-text right fine-print">(No credit checks)</p>
    <p class="sign-text tagline">Let us build<br>your dream home!</p>
    <p class="sign-text right call">Call</p>
    <p class="sign-text right phone">517-384-2296</p>
  </section>
</body>
</html>
```